Poster - Series of Poster Designs

We have a number of motivational quotes related to weight loss and fitness which need putting into a series of posters.
The designs need to:
- Reflect the current brand (see www.bluefernhaven.com.au)
- Be designed with scalability in mind to fit to A1, A3, A4, and A5. All portrait layout.
- Incorporate our logo
- Any images need to relfect the diversity of our clients ranging from 70kgs up to 200kgs.
- We have a stock of photos which can be used, or you can source your own (subject to budget approval)
Total of 26 posters in total, but all on the same design series (so effectively 1 design, with 26 applications).
The series of quotes are attached. An example quote would be:
-
"The difference between your body this week and next week is what you do for the next seven days to achieve your goals"
-
Our clients are a range of ages (20 - 60) and split male/female so colours should be neutral and reflect our orange/green branding. A modern feel but not super modern.
Output needs to be A3 ready to print with all source files included so that we can amend in the future.
There may be ongoing work for the right designer.

```html
<!DOCTYPE html>
<html lang="en">
<head>
<meta charset="utf-8">
<title>Bluefern Haven – Motivational Poster</title>
<link href="https://fonts.googleapis.com/css2?family=Roboto+Condensed:wght@300&display=swap" rel="stylesheet">
<style>
  :root {
    --sky-top: #8c9bb6;
    --sky-mid: #a3b0c6;
    --haze: #c7cfdc;
    --sunset-gold: #f4c27a;
    --sunset-orange: #ef9a55;
    --sea: #7f90ab;
    --sand: #8e9ab0;
    --base-blue: #4f6b8f;
    --base-deep: #46628a;
    --text-light: #f4f6fa;
    --brand-green: #8cc63f;
  }
  * { margin: 0; padding: 0; box-sizing: border-box; }
  html, body {
    width: 848px; height: 1200px; overflow: hidden;
    background: var(--base-blue);
  }
  .poster {
    position: relative;
    width: 848px; height: 1200px;
    overflow: hidden;
    background: linear-gradient(to bottom, var(--sky-top) 0%, var(--sky-mid) 20%, var(--base-blue) 75%, var(--base-deep) 100%);
    font-family: "Roboto Condensed", "Arial Narrow", sans-serif;
  }
  .hero-photo {
    position: absolute;
    left: 0; top: 260px;
    width: 848px; height: 640px;
    background: linear-gradient(to bottom,
      rgba(163,176,198,0) 0%,
      var(--haze) 16%,
      #e9d7bf 30%,
      var(--sunset-gold) 36%,
      var(--sunset-orange) 41%,
      var(--sea) 45%,
      #9aa6bb 54%,
      var(--sand) 70%,
      #6d83a3 86%,
      var(--base-blue) 100%);
  }
  .quote {
    position: absolute;
    top: 136px; left: 0; width: 848px;
    text-align: center;
    color: var(--text-light);
    font-weight: 300;
    font-size: 35px;
    letter-spacing: 0.4px;
    white-space: nowrap;
  }
  .quote .highlight {
    position: relative;
    display: inline-block;
  }
  .quote .highlight::after {
    content: "";
    position: absolute;
    left: 6px; right: 0; bottom: -6px;
    height: 2px;
    background: var(--brand-green);
  }
  .brand {
    position: absolute;
    top: 1100px; left: 0; width: 848px;
    text-align: center;
    color: var(--text-light);
    font-weight: 300;
  }
  .brand-name {
    display: block;
    font-size: 34px;
    line-height: 38px;
    letter-spacing: 2px;
  }
  .brand-tagline {
    display: block;
    font-size: 13px;
    letter-spacing: 2px;
    margin-top: 2px;
  }
</style>
</head>
<body>
  <main class="poster">
    <div class="hero-photo" role="img" aria-label="Group of retreat guests exercising on a beach at sunrise, with fitness balls and weights on the sand and the sun rising over the sea"></div>

    <p class="quote">every new day is another chance to <span class="highlight">change your life</span></p>

    <div class="brand">
      <span class="brand-name">BLUEFERN HAVEN</span>
      <span class="brand-tagline">WEIGHT LOSS RETREAT</span>
    </div>
  </main>
</body>
</html>
```